Corvanta Business cards template

We're looking for something modern and elegant. We are a reseller of technology (computers, datacenter, etc). Color theme would be "only" white with the incorporation of the blue that's present on our website (Corvanta.com) and logo file. We would like for the card to provide all the necessary info for the specific person (Phone#, fax#, email, name, website URL) . I'm attaching the logo file to this request. Please have it show Montreal/New York somewhere, without providing specific addresses.

Target Market(s)

All b2b

Industry/Entity Type

Business

Contact Information for Business Card

Please have the color scheme be represented by only the white and blue from our website (Corvanta.com) and logo. We would like to logo on the card, but not big and overwhelming. This card will be used as a template for anybody within the company, it should display the user's name, phone#, fax#, email, job title and website URL. Please have it show Montreal/New York somewhere, without providing our specific addresses. Really, we're looking for a clean, simple and elegant look.

Font styles to use
Serif

Requirements
Must have
• Please see card details
Nice to have
• Please see card details
Should not have
• Anything tacky or tagline.

```html
<!DOCTYPE html>
<html lang="en">
<head>
<meta charset="utf-8">
<title>Corvanta Business Card</title>
<link rel="stylesheet" href="https://fonts.googleapis.com/css2?family=Cormorant+Garamond:wght@500;600&family=Lora:wght@400&display=swap">
<style>
  :root {
    --page-bg: #e9e9eb;
    --card-bg: #f7f7f6;
    --brand-blue: #0b72bd;
    --accent-blue: #3d9be0;
    --text-light: #ffffff;
  }
  * { margin: 0; padding: 0; box-sizing: border-box; }
  html, body {
    width: 1200px; height: 900px; overflow: hidden;
    background: var(--page-bg);
  }
  .card {
    position: absolute;
    left: 150px; top: 173px;
    width: 900px; height: 554px;
    background: var(--card-bg);
    border-radius: 22px;
    overflow: hidden;
    box-shadow: 0 6px 24px rgba(0,0,0,0.12);
  }
  .card-shape {
    position: absolute; inset: 0;
    width: 100%; height: 100%;
  }
  .brand {
    position: absolute;
    right: 48px; top: 56px;
    font-family: "Cormorant Garamond", serif;
    font-weight: 600;
    font-size: 76px; line-height: 88px;
    letter-spacing: 4px;
    color: var(--brand-blue);
  }
  .person-name {
    position: absolute; left: 46px; top: 166px;
    font-family: "Cormorant Garamond", serif;
    font-weight: 600;
    font-size: 42px; line-height: 48px;
    letter-spacing: 1px;
    color: var(--text-light);
  }
  .person-title {
    position: absolute; left: 46px; top: 209px;
    font-family: "Lora", serif;
    font-size: 20px; line-height: 28px;
    color: var(--text-light);
  }
  .contact-list {
    position: absolute; left: 46px; top: 306px;
    list-style: none;
    font-family: "Lora", serif;
    font-size: 20px; color: var(--text-light);
  }
  .contact-list li {
    display: flex; align-items: center;
    height: 33px;
  }
  .contact-icon {
    width: 18px; height: 18px; margin-right: 14px;
    fill: var(--text-light);
  }
  .office {
    position: absolute; left: 46px; top: 451px;
    font-family: "Lora", serif;
    font-size: 20px; line-height: 33px;
    color: var(--text-light);
  }
</style>
</head>
<body>
  <div class="card">
    <svg class="card-shape" viewBox="0 0 650 400" preserveAspectRatio="none">
      <path fill="var(--brand-blue)" d="M0 16 Q110 -4 230 66 C360 148 500 285 495 342 C491 385 470 400 440 400 L0 400 Z"/>
      <path fill="none" stroke="var(--accent-blue)" stroke-width="2.5" d="M410 232 C465 290 470 372 300 388"/>
    </svg>

    <div class="brand">Corvanta</div>

    <div class="person-name">Daniel Mercer</div>
    <div class="person-title">Managing Director</div>

    <ul class="contact-list">
      <li>
        <svg class="contact-icon" viewBox="0 0 20 20"><path d="M2 7c0-3 3-4 8-4s8 1 8 4v2h-4V7H6v2H2z M4 10h12l1 7H3z M10 11.5a2.5 2.5 0 1 0 0.01 0z"/></svg>
        044-555 010 200
      </li>
      <li>
        <svg class="contact-icon" viewBox="0 0 20 20"><path d="M5 2h8l2 2v4H5z M3 9h14v9H3z M5 11h3v2H5z M10 11h5v1H10z M10 13h5v1H10z"/></svg>
        044-555 010 200
      </li>
      <li>
        <svg class="contact-icon" viewBox="0 0 20 20"><path d="M2 4h16v12H2z"/><path d="M2 4l8 7 8-7" fill="none" stroke="#0b72bd" stroke-width="1.6"/></svg>
        info@corvanta.com
      </li>
      <li>
        <svg class="contact-icon" viewBox="0 0 20 20"><circle cx="10" cy="10" r="8"/><path d="M6 7c2 0 3 1 2 3s1 3 0 5M12 4c-1 2 1 3 3 3M13 11c2 0 2 2 1 4" fill="none" stroke="#0b72bd" stroke-width="1.4"/></svg>
        www.corvanta.com
      </li>
    </ul>

    <div class="office">
      <div>Montreal, Quebec</div>
      <div>New York, New York</div>
    </div>
  </div>
</body>
</html>
```